website homepage design sample for tolvenra.com.au

Hello, I am looking to update my website to be simpler and more modern and to include space for my upcoming online courses. Please review my website tolvenra.com.au for an idea of me as a male psychologist, as well as my services. I would like it to be NOT too feminine. Target market is Men and women interested in couselling, life coaching, and online courses about relationships. Id like to keep the beach theme if possible but I am open to better ideas. thank you!

please see tolvenra.com.au for my current wordpress website.

Target Market(s)

Men and Women

Industry/Entity Type

psychology

Number of Pages Required

1 page

Requirements
Must have
• An "Online Training" Menu that includes links to "Map your Daybreak" , "Harbour and Lantern Journey," "Quiet Orchard Course" "Where Did All The Kites Go" "Gathering Willow Moments"

```html
<!DOCTYPE html>
<html lang="en">
<head>
<meta charset="utf-8">
<title>Tolvenra – Psychology &amp; Coaching</title>
<link rel="stylesheet" href="https://fonts.googleapis.com/css2?family=Fredoka:wght@500;600&family=Roboto:wght@400;500;700&display=swap">
<style>
:root{
  --teal:#1f8ba1;
  --teal-dark:#14687c;
  --teal-deep:#0f5a6c;
  --sky:#e1f5fa;
  --sage:#a9c9b6;
  --ink:#1c1c1c;
  --grey:#555;
  --white:#fff;
}
*{box-sizing:border-box;margin:0;padding:0}
html,body{width:1200px;height:4525px;overflow:hidden}
body{position:relative;background:var(--white);font-family:"Roboto",sans-serif;color:var(--ink)}
.abs{position:absolute}
.heading{font-family:"Fredoka",sans-serif;font-weight:600;letter-spacing:1px;text-transform:uppercase}
.btn{position:absolute;display:flex;align-items:center;justify-content:center;border-radius:30px;font-weight:700;font-size:14px;text-transform:uppercase;color:var(--white);text-decoration:none}
.btn-teal{background:linear-gradient(180deg,#2a9ab0,var(--teal-dark));box-shadow:0 4px 8px rgba(0,0,0,.2)}
.btn-sage{background:linear-gradient(180deg,#c4dccd,#96b9a4);color:var(--teal-dark);box-shadow:0 4px 8px rgba(0,0,0,.15)}
.ring{position:absolute;border:3px solid var(--teal);border-radius:50%}

/* top bar */
.topbar-offer{left:140px;top:0;width:580px;height:38px;background:var(--teal);clip-path:polygon(0 0,100% 0,95% 100%,0 100%);color:#fff;font-size:14px;font-weight:500;display:flex;align-items:center;justify-content:center}
.topbar-quiz{left:690px;top:0;width:370px;height:38px;background:#cfe6e2;clip-path:polygon(0 0,100% 0,95% 100%,8% 100%);color:var(--teal);font-size:14px;font-weight:500;display:flex;align-items:center;justify-content:center}

/* nav */
.brand{left:142px;top:58px;display:flex;align-items:center;gap:10px;font-family:"Fredoka",sans-serif;font-weight:600;font-size:24px;color:var(--teal);text-transform:uppercase}
.brand-dot{width:34px;height:34px;border-radius:50%;background:var(--teal)}
.nav{left:378px;top:72px;display:flex;gap:19px;font-size:12.5px;font-weight:500;text-transform:uppercase}
.nav .active{color:var(--teal)}
.search{left:1024px;top:68px;width:30px;height:30px;border-radius:50%;background:var(--teal)}

/* hero */
.hero{top:120px;left:0;width:1200px;height:627px;overflow:hidden}
.hero-photo{position:absolute;inset:0;background:linear-gradient(90deg,#6e6f6c 0%,#a9abaa 35%,#dfe2e2 60%,#f1f3f3 100%)}
.hero-title{left:638px;top:110px;font-family:"Fredoka",sans-serif;font-weight:600;font-size:60px;color:var(--teal);letter-spacing:1px}
.hero-sub{left:638px;top:193px;font-size:22px;font-weight:500}
.hero-next{left:638px;top:236px;font-size:15px;font-weight:500}
.hero-dots{left:1130px;top:258px;display:flex;flex-direction:column;gap:10px}
.hero-dots span{width:8px;height:8px;border-radius:50%;background:#9aa}
.hero-dots span.on{background:var(--teal)}

/* objectives */
.section-title{position:absolute;left:0;width:1200px;text-align:center;font-size:40px}
.objective{position:absolute;width:300px;height:300px;border-radius:50%;border:3px solid #7cbcca;background:var(--white);display:flex;flex-direction:column;align-items:center;padding-top:62px;text-align:center}
.objective .num{font-family:"Fredoka",sans-serif;font-weight:600;font-size:46px;color:var(--teal)}
.objective p{font-size:17px;font-weight:500;margin-top:12px;width:210px;line-height:1.4}
.objective.feature{background:var(--teal);border-color:var(--teal);color:#fff;padding-top:42px}
.objective.feature .num{color:#fff}

/* about */
.about-title{left:144px;top:1300px;font-size:40px}
.lead{position:absolute;font-size:24px;color:var(--teal);line-height:1.3}
.body-text{position:absolute;font-size:14px;color:var(--grey);line-height:1.72;text-align:justify}
.about-photo{left:611px;top:1291px;width:443px;height:440px;border-radius:40px;background:linear-gradient(135deg,#2b8c9c 0%,#5e8f92 50%,#146a7c 100%)}

/* service circles */
.service{position:absolute;border-radius:50%;border:10px solid var(--teal);overflow:hidden;display:flex;align-items:flex-end;justify-content:center;color:#fff;font-weight:700;font-size:22px;text-align:center;line-height:1.2;padding-bottom:52px;text-shadow:0 2px 4px rgba(0,0,0,.5)}

/* training cards */
.card{position:absolute;top:2328px;width:218px;height:206px;border-radius:26px;background:#fff;box-shadow:0 6px 14px rgba(0,0,0,.12);display:flex;flex-direction:column;align-items:center;text-align:center;font-size:13px;font-weight:700;text-transform:uppercase;line-height:1.45;padding-top:28px}
.card .icon{width:84px;height:70px;margin-bottom:36px;stroke:var(--teal);fill:none;stroke-width:3;stroke-linecap:round;stroke-linejoin:round}
.card.feature{background:var(--teal);color:#fff}
.card.feature .icon{stroke:#fff}

/* telehealth */
.tele-photo{left:0;top:2630px;width:1200px;height:422px;background:linear-gradient(90deg,#5b5148 0%,#8a7a68 30%,#7e9b4e 60%,#a9c27a 100%)}
.tele-frame{left:487px;top:2868px;width:667px;height:295px;border:2px solid var(--teal-dark)}
.tele-box{left:536px;top:2829px;width:664px;height:290px;background:#fff;padding:50px 0 0 78px}
.tele-box h2{font-size:25px;line-height:1.3;letter-spacing:1px}
.tele-box .lead{position:static;margin-top:22px}
.tele-box .tags{font-size:16px;margin-top:12px}

/* self worth */
.worth{left:0;top:3677px;width:1200px;height:620px;background:linear-gradient(90deg,#157a8e 0%,#106a7e 55%,#0b4a59 100%)}
.worth-text{left:144px;top:3844px;width:726px;font-size:14px;color:#fff;line-height:1.72}

/* footer */
.contact{left:180px;top:4337px;display:flex;gap:24px;font-size:16px;align-items:center}
.contact span{display:flex;align-items:center;gap:8px}
.badge{position:absolute;top:4420px;height:52px;border-radius:6px}
.social{position:absolute;top:4455px;width:30px;height:30px;border-radius:50%;background:var(--teal)}
</style>
</head>
<body>

<!-- top bar -->
<div class="abs topbar-offer">SELF ESTEEM COURSE ONLY $47</div>
<div class="abs topbar-quiz">MAP YOUR DAYBREAK</div>

<!-- navigation -->
<div class="abs brand"><span class="brand-dot"></span>Tolvenra</div>
<nav class="abs nav">
  <span class="active">Home</span><span>About</span><span>Counselling &amp; Therapy</span><span>Online Training</span><span>Blog</span><span>Contact</span><span>Bookings</span>
</nav>
<div class="abs search"></div>

<!-- hero -->
<section class="abs hero">
  <div class="hero-photo" role="img" aria-label="Psychologist seated on a sofa in a bright consulting room"></div>
  <svg class="abs" style="left:0;top:0" width="1200" height="627" viewBox="0 0 1200 627">
    <path d="M0 405 Q300 640 610 600 Q900 560 1200 385 L1200 627 L0 627Z" fill="#fff"/>
    <path d="M0 405 Q300 640 610 600 Q900 560 1200 385" fill="none" stroke="#1f8ba1" stroke-width="7"/>
  </svg>
  <div class="abs hero-title">TOLVENRA</div>
  <div class="abs hero-sub">PSYCHOLOGY &amp; COACHING</div>
  <div class="abs hero-next">NEXT AVAILABLE APPOINTMENT: WITHIN 7 DAYS</div>
  <a class="btn btn-teal" style="left:641px;top:284px;width:411px;height:56px;font-size:16px">Harbour and Lantern Journey</a>
  <a class="btn btn-sage" style="left:641px;top:358px;width:411px;height:52px;font-size:16px">Free Self Confidence Masterclass</a>
  <div class="abs hero-dots"><span></span><span class="on"></span><span></span></div>
</section>

<!-- edge rings -->
<div class="ring" style="left:-120px;top:760px;width:220px;height:220px"></div>
<div class="ring" style="left:1135px;top:640px;width:160px;height:160px"></div>
<div class="ring" style="left:1135px;top:1450px;width:160px;height:160px"></div>
<div class="ring" style="left:-120px;top:1710px;width:220px;height:220px"></div>
<div class="ring" style="left:24px;top:2580px;width:100px;height:100px"></div>
<div class="ring" style="left:-110px;top:2960px;width:220px;height:220px"></div>
<div class="ring" style="left:634px;top:3264px;width:150px;height:150px"></div>
<div class="ring" style="left:1103px;top:4258px;width:150px;height:150px"></div>
<div class="ring" style="left:-60px;top:4300px;width:100px;height:100px"></div>

<!-- objectives -->
<h2 class="section-title heading" style="top:808px">Tolvenra has 3 objectives</h2>
<div class="objective" style="left:142px;top:906px"><span class="num">01</span><p>Alleviate distress</p></div>
<div class="objective feature" style="left:449px;top:906px"><span class="num">02</span><p>Take the next step in helping you create a fulfilling, meaningful and enjoyable life through coaching and positive</p></div>
<div class="objective" style="left:758px;top:906px"><span class="num">03</span><p>Learn, implement and habitualise advanced performance strategies for lasting change</p></div>

<!-- about -->
<h2 class="abs heading about-title">About</h2>
<p class="lead" style="left:144px;top:1355px;width:470px">An experienced Gold Coast Psychologist,<br>also available online.</p>
<p class="body-text" style="left:144px;top:1435px;width:418px">Unfortunately, we all go through periods of crisis in our lives. When we find ourselves struggling for an extended period, we can use bit of help to work through barriers that stand in our way. Counselling or psychotherapy can help. Contact Daniel, your Gold Coast Psychologist.</p>
<p class="body-text" style="left:144px;top:1578px;width:418px">Daniel has 15 years experience in providing counselling and psychotherapy to people from all of walks of life. Daniel understands the different challenges that people of all backgrounds face in coming to seek help and has a variety of treatments to help.</p>
<a class="btn btn-teal" style="left:144px;top:1722px;width:218px;height:49px">Book Appointment</a>
<div class="abs about-photo" role="img" aria-label="Photo of the psychologist in a counselling session"></div>

<!-- service circles over curved band -->
<svg class="abs" style="left:0;top:2060px" width="1200" height="570" viewBox="0 0 1200 570">
  <path d="M0 130 Q600 -90 1200 130 L1200 570 L0 570Z" fill="#e1f5fa"/>
  <path d="M0 130 Q300 10 520 20" fill="none" stroke="#1f8ba1" stroke-width="4"/>
  <path d="M980 20 Q1100 50 1200 100" fill="none" stroke="#1f8ba1" stroke-width="6"/>
</svg>
<div class="service" style="left:162px;top:1854px;width:274px;height:274px;background:linear-gradient(160deg,#8a7a6a,#2a4a55)" role="img" aria-label="Counselling session between two people">Psychological<br>Counselling</div>
<div class="service" style="left:430px;top:1822px;width:338px;height:338px;border-color:#0f5a6c;background:linear-gradient(160deg,#a29884,#244e52)" role="img" aria-label="Psychologist speaking with a client">Self Esteem<br>Course</div>
<div class="service" style="left:758px;top:1854px;width:274px;height:274px;background:linear-gradient(160deg,#9aa4a8,#364a52)" role="img" aria-label="Webinar playing on a laptop screen">FREE Self<br>Esteem Webinar</div>

<!-- online training -->
<h2 class="section-title heading" style="top:2240px">Online Training</h2>
<div class="card" style="left:26px">
  <svg class="icon" viewBox="0 0 84 70"><rect x="26" y="6" width="32" height="44" rx="3"/><path d="M33 18l3 3 5-6M33 30l3 3 5-6M46 19h6M46 31h6M18 62h48"/></svg>
  Map your<br>Daybreak</div>
<div class="card" style="left:258px">
  <svg class="icon" viewBox="0 0 84 70"><circle cx="22" cy="40" r="7"/><circle cx="42" cy="30" r="7"/><circle cx="62" cy="40" r="7"/><path d="M10 64c2-10 22-10 24 0M50 64c2-10 22-10 24 0M32 50c2-8 18-8 20 0"/><rect x="50" y="4" width="22" height="14" rx="2"/></svg>
  Harbour and<br>Lantern Journey</div>
<div class="card feature" style="left:492px">
  <svg class="icon" viewBox="0 0 84 70"><path d="M42 8l5 12 12 2-9 8 3 12-11-7-11 7 3-12-9-8 12-2z"/><path d="M14 14l3 6M70 14l-3 6M20 58h44"/></svg>
  Quiet Orchard<br>Course</div>
<div class="card" style="left:724px">
  <svg class="icon" viewBox="0 0 84 70"><circle cx="22" cy="22" r="9"/><circle cx="62" cy="40" r="9"/><path d="M8 62c2-14 26-14 28 0M48 66c2-10 26-10 28 0M36 12h16l-4-4M52 12l-4 4"/></svg>
  Where Did All<br>The Kites Go</div>
<div class="card" style="left:956px">
  <svg class="icon" viewBox="0 0 84 70"><circle cx="26" cy="34" r="14"/><circle cx="58" cy="34" r="14"/><path d="M14 10q28-12 56 0M26 58v8M58 58v8"/></svg>
  Gathering Willow<br>Moments</div>

<!-- telehealth -->
<div class="abs tele-photo" role="img" aria-label="Psychologist listening to a client, garden in background"></div>
<div class="abs tele-frame"></div>
<div class="abs tele-box">
  <h2 class="heading">Gold Coast Psychologist<br>also offering Australia<br>wide Telehealth</h2>
  <p class="lead">Healthcover rebates available</p>
  <p class="tags">Experienced – Caring – Understanding – Effective – Affordable</p>
</div>

<!-- practitioner -->
<h2 class="abs heading" style="left:144px;top:3232px;font-size:40px;line-height:1.15">Tolvenra by<br>Daniel Hartley</h2>
<p class="lead" style="left:144px;top:3330px">Psychologist Gold Coast</p>
<p class="body-text" style="left:144px;top:3378px;width:418px">Congratulations on taking the first step to overcoming your barriers and being who you want to be. At Tolvenra, we are focused on your mental wellness. Tolvenra is open to anyone looking for a Gold Coast Psychologist or other therapist to help them overcome barriers and find fulfillment in their lives. We also offer online programs.</p>
<a class="btn btn-teal" style="left:144px;top:3553px;width:146px;height:49px">Read More</a>
<a class="btn btn-sage" style="left:298px;top:3553px;width:146px;height:49px">Book Online</a>
<div class="abs" style="left:660px;top:3231px;width:394px;height:394px;border-radius:50%;background:radial-gradient(circle at 50% 40%,#b79b8a,#5a5554 70%)" role="img" aria-label="Portrait of the psychologist"></div>

<!-- self worth -->
<div class="abs worth" role="img" aria-label="Silhouette of a person with raised arms against mountains at dusk"></div>
<h2 class="abs heading" style="left:144px;top:3765px;font-size:40px;color:#fff">Finding Self Worth</h2>
<p class="abs worth-text">Wondering where to start? Watch our free Self Worth Webinar<br>Wondering how your self Esteem stacks up? take our Assertiveness Quiz.<br>Interested in a what psychotherapy can offer but not quite ready? Try our Self Esteem Course<br>Your Online or Gold Coast Psychologist should not only be about moving away from what makes you sad, but moving towards what makes you happy, resilient engaged and fulfilled. At Tolvenra, Daniel combines evidence-based treatment from both mental illness and mental wellness fields to take you all the way from anxiety and depression to strength and success.</p>
<a class="btn" style="left:144px;top:4032px;width:378px;height:48px;background:#fff;color:var(--teal-dark);font-size:13px">5 Steps Closer to Self Esteem</a>

<!-- footer -->
<svg class="abs" style="left:0;top:4140px" width="1200" height="385" viewBox="0 0 1200 385">
  <path d="M0 160 Q600 -20 1200 140 L1200 385 L0 385Z" fill="#e1f5fa"/>
</svg>
<div class="abs brand" style="left:505px;top:4244px"><span class="brand-dot"></span>Tolvenra</div>
<div class="abs contact">
  <span><svg width="16" height="16" viewBox="0 0 16 16"><path d="M8 1a5 5 0 0 0-5 5c0 4 5 9 5 9s5-5 5-9a5 5 0 0 0-5-5zm0 7a2 2 0 1 1 0-4 2 2 0 0 1 0 4z" fill="#1f8ba1"/></svg>48 Marlow Ave. Seabrook</span>
  <span><svg width="16" height="16" viewBox="0 0 16 16"><path d="M3 1l3 3-2 2c1 2 3 4 5 5l2-2 3 3-2 3C6 14 2 10 1 4z" fill="#1f8ba1"/></svg>0491 570 218</span>
  <span><svg width="16" height="16" viewBox="0 0 16 16"><rect x="2" y="5" width="12" height="9" rx="1" fill="#1f8ba1"/><rect x="4" y="1" width="8" height="4" fill="#1f8ba1"/></svg>Fax. (07) 3000 8142</span>
  <span><svg width="16" height="16" viewBox="0 0 16 16"><circle cx="8" cy="8" r="7" fill="#1f8ba1"/><path d="M8 4v4l3 2" stroke="#fff" stroke-width="1.6" fill="none"/></svg>8:00am - 7:00pm (appt. Only)</span>
</div>
<div class="badge" style="left:144px;width:110px;background:#d8c890"></div>
<div class="badge" style="left:286px;width:104px;background:#6fb54a"></div>
<p class="abs" style="left:608px;top:4418px;font-size:13px">© 2024 Tolvenra.All Rights Reserved &nbsp;|&nbsp; Privacy Policy &nbsp;|&nbsp; Terms of Use</p>
<div class="social" style="left:916px"></div>
<div class="social" style="left:952px;background:#a9c9b6"></div>
<div class="social" style="left:988px"></div>
<div class="social" style="left:1024px"></div>

</body>
</html>
```